Tidewell Cargo Links Website

We require a prominent webpage for a new concept on an old idea. We are a freight forwarding company in the Bahamas that will streamline the import process in the Bahamas for clients while offering both airfreight and seafreight import and export services . We would like the final design to communicate a professional image with stable service offering. Please view www.korvanfreight.example to see an example of what we require. Also view the site www.pemla.tariffgate.example and dorvelin.example. We will requier integration with these and other websites.

Target Market(s)

Small (<100) and medium (100-500) commercial businesses that require full importation services.

Industry/Entity Type

Freight Forwarding

Coding

Coded - Design and coding required

Number of Pages Required

5+ page

Colors

Designer to choose colors to be used in the design.

Requirements
Must have
• Core Website Development – Front End
• 1. Website Design
• 2. Coding and Development
• 4. Graphics
• 5. Social Media Integrations
• 6. Email Integration
• 7. Security / SSL Integrations
• 8. User Dashboard / Account
• 9. Customer Signup Integration
• 10. eCommerceOnlinePayment
• 11. XML–APIDevelopmentforDorvelin
• 12. DorvelinIntegrations

```html
<!DOCTYPE html>
<html lang="en">
<head>
<meta charset="utf-8">
<title>Tidewell Cargo Links</title>
<link rel="stylesheet" href="https://fonts.googleapis.com/css2?family=Exo+2:wght@500;600;700;800&family=Open+Sans:wght@400;600;700&display=swap">
<style>
:root{
  --navy:#1d3553;
  --navy-dark:#142840;
  --teal:#3a9fa6;
  --teal-deep:#3c6f7b;
  --red:#e2452f;
  --beige:#f6f2ed;
  --ink:#3a3f47;
  --muted:#6b717a;
  --white:#ffffff;
  --line:#d9d4ce;
}
*{box-sizing:border-box;margin:0;padding:0}
html,body{width:1200px;height:4749px;overflow:hidden}
body{font-family:"Open Sans",Arial,sans-serif;color:var(--ink);background:var(--white);font-size:15px;line-height:1.55}
.page{position:relative;width:1200px;height:4749px}
section,header,footer{position:relative;width:1200px;overflow:hidden}
.heading-font{font-family:"Exo 2",Arial,sans-serif}

/* header */
.site-header{height:175px;background:var(--white)}
.brand{position:absolute;left:48px;top:52px;display:flex;align-items:center;gap:14px}
.brand-dot{width:60px;height:60px;border-radius:50%;background:var(--navy)}
.brand-name{font-family:"Exo 2",Arial,sans-serif;font-weight:700;font-size:24px;color:var(--navy);line-height:1.1;width:170px}
.top-contacts{position:absolute;right:48px;top:22px;display:flex;gap:34px;font-size:12px;color:var(--navy);line-height:1.3}
.top-contacts b{display:block;font-size:11px;letter-spacing:.5px}
.main-nav{position:absolute;right:48px;top:104px;display:flex;align-items:center;gap:8px}
.nav-item{font-family:"Exo 2",Arial,sans-serif;font-weight:600;font-size:14px;color:var(--navy);padding:10px 14px;display:flex;align-items:center;gap:7px;letter-spacing:.4px}
.nav-item svg{width:16px;height:16px}
.nav-item.active{color:var(--teal);background:#eaf5f6;border-radius:3px}
.btn-quote{background:var(--red);color:var(--white);font-family:"Exo 2",Arial,sans-serif;font-weight:700;font-size:14px;padding:12px 20px;border-radius:3px;margin-left:8px;letter-spacing:.4px}

/* hero */
.hero{height:570px}
.hero-photo{position:absolute;inset:0;background:linear-gradient(180deg,#b9cbd8 0%,#8fa9bd 35%,#3f6f8e 60%,#234f6d 100%)}
.slider-dots{position:absolute;bottom:26px;left:50%;transform:translateX(-50%);display:flex;gap:10px}
.slider-dots span{width:22px;height:5px;background:rgba(255,255,255,.5)}
.slider-dots span:first-child{background:var(--white)}

/* tagline */
.tagline{height:175px;background:var(--navy)}
.tagline-title{position:absolute;left:58px;top:44px;font-family:"Exo 2",Arial,sans-serif;font-weight:800;font-size:46px;line-height:1.1;color:var(--white);letter-spacing:.5px}
.tagline-title .t-teal{color:var(--teal)}
.tagline-title .t-red{color:var(--red)}
.tagline-text{position:absolute;left:528px;top:44px;width:600px;color:var(--white);font-size:17px;line-height:1.5}

/* section titles */
.section-mark{width:44px;height:44px;border-radius:50%;background:var(--red);margin:0 auto}
.section-title{font-family:"Exo 2",Arial,sans-serif;font-weight:700;font-size:27px;color:var(--navy);text-align:center;letter-spacing:.5px;margin-top:14px}
.section-title .accent{color:var(--teal)}
.section-lead{width:1000px;margin:30px auto 0;text-align:center;font-size:15px;color:var(--ink)}

/* forwarding */
.forwarding{height:665px;background:var(--beige);padding-top:70px}
.service-cols{display:flex;justify-content:space-between;width:1040px;margin:64px auto 0}
.service{width:300px}
.service-icon{width:100px;height:100px;border-radius:50%;border:4px solid var(--navy);display:flex;align-items:center;justify-content:center;margin:0 0 20px 90px}
.service-icon svg{width:52px;height:52px}
.service h3{font-family:"Exo 2",Arial,sans-serif;font-weight:700;font-size:16px;color:var(--navy);margin-bottom:6px}
.service p{font-size:14px;line-height:1.5}

/* consolidation */
.consolidation{height:570px;background:var(--white);padding-top:95px}
.consol-row{position:relative;width:1120px;height:290px;margin:20px auto 0}
.consol-item{position:absolute;top:40px;width:290px;font-size:14px}
.consol-item h3{font-family:"Exo 2",Arial,sans-serif;font-weight:700;font-size:16px;color:var(--teal)}
.consol-item.left{left:0}
.consol-item.right{right:0}
.consol-badge{position:absolute;top:50px;width:52px;height:52px;background:var(--red);border-radius:6px;display:flex;align-items:center;justify-content:center}
.consol-badge svg{width:30px;height:30px}
.consol-badge.left{left:300px}
.consol-badge.right{right:300px}
.consol-art{position:absolute;left:380px;top:10px;width:360px;height:290px;border-radius:180px 180px 0 0;background:linear-gradient(180deg,#eef1f4 0%,#cdd6df 60%,#9fb0c2 100%)}

/* customs */
.customs{height:585px;background:linear-gradient(180deg,rgba(54,110,122,.92),rgba(48,98,110,.94)),linear-gradient(90deg,#5d8a95,#2f5d6a)}
.customs .inner{padding-top:80px}
.customs .section-mark{background:var(--white)}
.customs .section-title{color:var(--white)}
.customs .section-lead{color:#e6f1f2;width:960px;margin-top:22px}
.customs-grid{display:grid;grid-template-columns:520px 520px;column-gap:60px;row-gap:50px;width:1100px;margin:60px auto 0}
.customs-item{display:flex;align-items:center;gap:24px;color:var(--white);font-weight:600;font-size:15px}
.customs-icon{flex:none;width:84px;height:84px;border-radius:50%;background:var(--white);display:flex;align-items:center;justify-content:center}
.customs-icon svg{width:42px;height:42px}

/* warehousing */
.warehousing{height:520px;background:var(--white)}
.wh-head{position:absolute;left:70px;top:80px;display:flex;align-items:center;gap:16px}
.wh-head .section-mark{margin:0}
.wh-head .section-title{margin:0;color:var(--teal)}
.wh-body{position:absolute;left:70px;top:160px;width:640px;font-size:14px}
.wh-body ul{list-style:none;margin-top:14px}
.wh-body li{line-height:1.6}
.wh-photo{position:absolute;left:780px;top:70px;width:310px;height:310px;border-radius:50%;border:8px solid #e7edf2;background:radial-gradient(circle at 50% 45%,#9fc4e4 0%,#3f77b0 55%,#1f4a7d 100%)}

/* news */
.news{height:620px;background:var(--beige);padding-top:95px}
.news-cards{display:flex;justify-content:space-between;width:1100px;margin:52px auto 0}
.news-card{width:350px;text-align:center}
.news-photo{height:160px}
.news-photo.one{background:linear-gradient(180deg,#8fb8e0,#dfe7ee 60%,#9aa3ad)}
.news-photo.two{background:linear-gradient(180deg,#b6d5ee,#6d8fb3 55%,#7b2f2a 80%,#2f4a68)}
.news-photo.three{background:linear-gradient(180deg,#dfe4ea,#9fa8b3 60%,#5a6573)}
.news-card h3{font-family:"Exo 2",Arial,sans-serif;font-weight:700;font-size:21px;color:var(--teal);margin:16px 0 8px}
.news-card p{font-size:14px;text-align:left;padding:0 4px}
.btn-read{display:inline-block;margin-top:14px;background:var(--red);color:var(--white);font-weight:600;font-size:13px;padding:8px 26px;border-radius:2px}

/* quote */
.quote{height:520px;background:linear-gradient(180deg,rgba(62,112,124,.9),rgba(40,82,96,.95)),linear-gradient(90deg,#6f97a2,#2b5563)}
.quote .inner{padding-top:65px}
.quote-head{display:flex;align-items:center;justify-content:center;gap:16px}
.quote-head .section-mark{margin:0;background:var(--white)}
.quote-head .section-title{margin:0;color:var(--white)}
.quote-form{width:1100px;margin:44px auto 0}
.form-row{display:flex;gap:18px}
.field{flex:1;height:50px;background:var(--white);border-radius:3px;padding:14px 16px;font-size:14px;color:var(--muted)}
.field.message{height:134px;margin-top:18px}
.btn-send{display:block;width:200px;margin:26px auto 0;text-align:center;background:var(--red);color:var(--white);font-weight:600;font-size:16px;padding:11px 0;border-radius:3px;border:2px solid #f3c3bb}

/* footer */
.site-footer{height:320px;background:var(--white)}
.footer-brand{position:absolute;left:80px;top:80px;display:flex;flex-direction:column;align-items:center;gap:14px}
.footer-brand .brand-name{text-align:center;width:200px}
.socials{display:flex;gap:10px}
.socials span{width:20px;height:20px;border-radius:50%;background:var(--navy)}
.footer-col{position:absolute;top:60px;font-size:13px;color:var(--ink)}
.footer-col h4{font-family:"Exo 2",Arial,sans-serif;font-weight:700;font-size:15px;color:var(--navy);letter-spacing:.5px;border-bottom:1px solid var(--line);padding-bottom:8px;margin-bottom:16px;width:240px}
.footer-col.links{left:370px}
.footer-col.links h4{width:150px}
.footer-col.bahamas{left:540px}
.footer-col.usa{left:850px}
.contact-line{display:flex;gap:12px;margin-bottom:14px;line-height:1.4}
.contact-line svg{flex:none;width:20px;height:20px}
.copyright{position:absolute;left:0;bottom:0;width:1200px;height:29px;background:var(--navy);color:var(--white);font-size:11px;text-align:center;line-height:29px;letter-spacing:.4px}
</style>
</head>
<body>
<div class="page">

<header class="site-header">
  <div class="brand"><span class="brand-dot"></span><span class="brand-name">Tidewell Cargo Links</span></div>
  <div class="top-contacts">
    <div><b>BAHAMAS</b>(242) 555-0148</div>
    <div><b>USA</b>(305) 555-0172</div>
  </div>
  <nav class="main-nav">
    <span class="nav-item active"><svg viewBox="0 0 16 16"><path d="M2 8 8 2l6 6M4 7v7h8V7" fill="none" stroke="currentColor" stroke-width="1.8"/></svg>HOME</span>
    <span class="nav-item"><svg viewBox="0 0 16 16"><circle cx="8" cy="8" r="6.5" fill="none" stroke="currentColor" stroke-width="1.6"/><path d="M8 7v5M8 4.5v.5" stroke="currentColor" stroke-width="1.8"/></svg>ABOUT</span>
    <span class="nav-item"><svg viewBox="0 0 16 16"><circle cx="8" cy="8" r="5" fill="none" stroke="currentColor" stroke-width="3" stroke-dasharray="2.5 1.5"/></svg>SERVICES</span>
    <span class="nav-item"><svg viewBox="0 0 16 16"><path d="M2 3h10v11H3a1 1 0 0 1-1-1zM12 6h2v7a1 1 0 0 1-2 0M4 6h6M4 9h6M4 12h4" fill="none" stroke="currentColor" stroke-width="1.4"/></svg>NEWS</span>
    <span class="nav-item"><svg viewBox="0 0 16 16"><path d="M4 1.5 6.5 5 5 6.5c1 2 2.5 3.5 4.5 4.5L11 9.5l3.5 2.5-1.5 2.5C8 14 2 8 1.5 3z" fill="currentColor"/></svg>CONTACT</span>
    <span class="btn-quote">REQUEST A QUOTE</span>
  </nav>
</header>

<section class="hero">
  <div class="hero-photo" role="img" aria-label="Photograph of a loaded container ship sailing on open sea with a distant coastline"></div>
  <div class="slider-dots"><span></span><span></span><span></span><span></span></div>
</section>

<section class="tagline">
  <h1 class="tagline-title"><span class="t-teal">YOUR</span> <span class="t-red">FORWARDING</span><br>SOLUTION PROVIDER</h1>
  <p class="tagline-text">Our mission is to constantly exceed customer expectations by providing superior <b>Freight forwarding and global transportation solutions including customs clearance and logistics services.</b></p>
</section>

<section class="forwarding">
  <div class="section-mark"></div>
  <h2 class="section-title"><span class="accent">FREIGHT FORWARDING</span> &amp; LOGISTICS</h2>
  <p class="section-lead">We offer Freight Forwarding &amp; Logistics Services that include International Freight Forwarding, Import &amp; Export of Air Cargo, Import &amp; Export of Sea Cargo and Multi-modal Transshipment. Our time-bound service is designed to meet your on-time requirements. Our Logistics &amp; Freight Forwarding services are executed by expert manpower and in a well-planned manner to ensure safe delivery of goods.</p>
  <div class="service-cols">
    <div class="service">
      <div class="service-icon"><svg viewBox="0 0 52 52"><path d="M6 30h40l-6 12H12z" fill="var(--red)"/><rect x="12" y="20" width="8" height="10" fill="var(--navy)"/><rect x="22" y="20" width="8" height="10" fill="var(--navy)"/><rect x="32" y="20" width="8" height="10" fill="var(--navy)"/><rect x="17" y="12" width="8" height="8" fill="var(--navy)"/><rect x="27" y="12" width="8" height="8" fill="var(--navy)"/></svg></div>
      <h3>Ocean Freight Services</h3>
      <p>TCL Ltd. offers inbound and outbound services for both LCL (Less Than Container Load) and FCL (Full Container Load). We have special contract rates with some of the leading main line operators with service coverage to and from all major ports and destinations. A multi modal door-door transportation model is also available.</p>
    </div>
    <div class="service">
      <div class="service-icon"><svg viewBox="0 0 52 52"><path d="M46 10 30 24l4 18-4 3-8-14-8 7 1 7-3 2-4-8-8-4 2-3 7 1 7-8-14-8 3-4 18 4L42 6z" fill="var(--teal)"/></svg></div>
      <h3>Air Freight Services</h3>
      <p>To meet all your global transportation requirements, we provide freight forwarding services that can handle all air freight shipment needs around the world from small to largest consignments in most professional and authentic manner having swiftest quality.</p>
    </div>
    <div class="service">
      <div class="service-icon"><svg viewBox="0 0 52 52"><rect x="10" y="16" width="32" height="26" fill="var(--red)"/><path d="M10 16l16-8 16 8" fill="none" stroke="var(--navy)" stroke-width="3"/><path d="M26 16v26" stroke="var(--white)" stroke-width="3"/></svg></div>
      <h3>Domestic Shipping Services</h3>
      <p>The domestic shipment services provided by us are the forte of our company. These shipping services are specially designed keeping in mind the uniqueness of our archipelago. The domestic shipment team is committed to the seamless, safe and secure movement of cargo or consignment.</p>
    </div>
  </div>
</section>

<section class="consolidation">
  <div class="section-mark"></div>
  <h2 class="section-title"><span class="accent">FREIGHT CONSOLIDATION</span> SERVICES</h2>
  <p class="section-lead">The Freight Consolidation Services for shipments are the cost effective way to transport low volume cargo. By grouping your shipment with others to fill a standard container, you avoid the cost of shipping an entire container on your own. Cargo freight consolidation is a cost effective supply chain solution. The consolidated shipments receive the same benefits as full container load shipments with our world class logistics team, global network and local experts at every destination.</p>
  <div class="consol-row">
    <div class="consol-item left"><h3>Inbound Groupage</h3>Working through an extensive global network of associates and innovative routings, TCL Ltd. ensures that inbound freight into The Bahamas is economical, effective and time bound as far as deliveries are concerned.</div>
    <div class="consol-badge left"><svg viewBox="0 0 30 30"><rect x="5" y="8" width="20" height="16" fill="none" stroke="#fff" stroke-width="2.4"/><path d="M5 14h20M12 8v16" stroke="#fff" stroke-width="2"/></svg></div>
    <div class="consol-art" role="img" aria-label="Illustration of a cargo ship bow framed by a compass arc"></div>
    <div class="consol-badge right"><svg viewBox="0 0 30 30"><path d="M4 20h16V10H4zM20 14h4l3 4v2h-7" fill="none" stroke="#fff" stroke-width="2.2"/><circle cx="9" cy="22" r="2.5" fill="#fff"/><circle cx="22" cy="22" r="2.5" fill="#fff"/></svg></div>
    <div class="consol-item right"><h3>In Bound Door To Door Logistics</h3>TCL Ltd. specializes in offering services that span, Shipping Documentation, Custom Clearances, Cargo Insurance, Warehousing and Local Distribution as a part of its Door-to-Door Logistics Service.</div>
  </div>
</section>

<section class="customs">
  <div class="inner">
    <div class="section-mark"></div>
    <h2 class="section-title">CUSTOMS CLEARANCE SERVICES</h2>
    <p class="section-lead">The Import and Export Customs Clearance Services offered by TCL Ltd. supports faster hassle-free clearance of shipments. We utilize our expertise and latest technology and ensure that the supply chain of our clients remain compliant.</p>
    <div class="customs-grid">
      <div class="customs-item"><span class="customs-icon"><svg viewBox="0 0 42 42"><rect x="6" y="8" width="30" height="20" fill="none" stroke="var(--red)" stroke-width="3"/><path d="M21 28v8M13 36h16" stroke="var(--navy)" stroke-width="3"/></svg></span>Foreign Trade Zone Consulting</div>
      <div class="customs-item"><span class="customs-icon"><svg viewBox="0 0 42 42"><path d="M10 4h16l8 8v26H10z" fill="none" stroke="var(--red)" stroke-width="3"/><path d="M15 20h12M15 26h12M15 32h8" stroke="var(--navy)" stroke-width="2.5"/></svg></span>Import Documentation preparation for Home Consumption, Transhipments and Temporary Admissions</div>
      <div class="customs-item"><span class="customs-icon"><svg viewBox="0 0 42 42"><rect x="9" y="5" width="24" height="32" rx="2" fill="none" stroke="var(--red)" stroke-width="3"/><rect x="13" y="10" width="16" height="6" fill="var(--navy)"/><path d="M14 23h3M20 23h3M26 23h2M14 30h3M20 30h3M26 30h2" stroke="var(--navy)" stroke-width="3"/></svg></span>Calculation and payment of taxes, duties, and excises</div>
      <div class="customs-item"><span class="customs-icon"><svg viewBox="0 0 42 42"><path d="M8 16h26v16H8z" fill="none" stroke="var(--red)" stroke-width="3"/><path d="M12 16V6h18v10M12 26h18v10H12z" fill="none" stroke="var(--navy)" stroke-width="2.5"/></svg></span>Import and export Clearance Services Available</div>
    </div>
  </div>
</section>

<section class="warehousing">
  <div class="wh-head"><span class="section-mark"></span><h2 class="section-title">WAREHOUSING</h2></div>
  <div class="wh-body">
    <p>We offer dedicated warehousing services to our clients that helps them in easy handling of their imported and exported goods. The cargo and goods are easily segregated in a quick and effective manner that results in covering any unnecessary delay.</p>
    <ul>
      <li>- Need a place to store goods &amp; products? Postpone High Customs Expense?</li>
      <li>- Inventory control at storage facilities in South Florida and Nassau, Bahamas</li>
      <li>- Inventory is carefully documented</li>
      <li>- Proper packaging and labeling solutions</li>
      <li>- Reports available upon request</li>
      <li>- Ability to expand facilities as needed with ease</li>
      <li>- Customization of your warehouse and transportation services</li>
      <li>- Forklift and crane equipment to handle all incoming and outgoing shipments</li>
    </ul>
  </div>
  <div class="wh-photo" role="img" aria-label="Photograph of a tall warehouse aisle with stacked pallet racks"></div>
</section>

<section class="news">
  <div class="section-mark"></div>
  <h2 class="section-title"><span class="accent">LATEST</span> NEWS</h2>
  <div class="news-cards">
    <article class="news-card">
      <div class="news-photo one" role="img" aria-label="Photograph of a cargo plane being loaded on an airport apron"></div>
      <h3>News Title #1</h3>
      <p>Lorem ipsum dolor sit amet, consectetuer adipiscing elit, sed diam nonummy nibh euismod tincidunt ut laoreet dolore magna aliquam.</p>
      <span class="btn-read">Read More</span>
    </article>
    <article class="news-card">
      <div class="news-photo two" role="img" aria-label="Photograph of a container ship at sea under a blue sky"></div>
      <h3>News Title #2</h3>
      <p>Lorem ipsum dolor sit amet, consectetuer adipiscing elit, sed diam nonummy nibh euismod tincidunt ut laoreet dolore magna aliquam.</p>
      <span class="btn-read">Read More</span>
    </article>
    <article class="news-card">
      <div class="news-photo three" role="img" aria-label="Photograph of a business meeting in a bright office"></div>
      <h3>News Title #3</h3>
      <p>Lorem ipsum dolor sit amet, consectetuer adipiscing elit, sed diam nonummy nibh euismod tincidunt ut laoreet dolore magna aliquam.</p>
      <span class="btn-read">Read More</span>
    </article>
  </div>
</section>

<section class="quote" role="img" aria-label="Tinted photograph of a container port with cranes behind the quote form">
  <div class="inner">
    <div class="quote-head"><span class="section-mark"></span><h2 class="section-title">REQUEST A QUOTE</h2></div>
    <div class="quote-form">
      <div class="form-row"><div class="field">Your Name</div><div class="field">Your Email</div><div class="field">Your Subject</div></div>
      <div class="field message">Message</div>
      <span class="btn-send">Send Message</span>
    </div>
  </div>
</section>

<footer class="site-footer">
  <div class="footer-brand">
    <span class="brand-dot"></span>
    <span class="brand-name">Tidewell Cargo Links</span>
    <div class="socials"><span></span><span></span><span></span></div>
  </div>
  <div class="footer-col links">
    <h4>QUICK LINKS</h4>
    <div>Home</div><div>About</div><div>Services</div><div>News</div><div>Contact</div><div>Request a Quote</div>
  </div>
  <div class="footer-col bahamas">
    <h4>BAHAMAS</h4>
    <div class="contact-line"><svg viewBox="0 0 20 20"><path d="M10 1a6 6 0 0 1 6 6c0 5-6 12-6 12S4 12 4 7a6 6 0 0 1 6-6z" fill="var(--navy)"/><circle cx="10" cy="7" r="2" fill="#fff"/></svg><span>P.O. Box SP-40217<br>Nassau, N.P., Bahamas</span></div>
    <div class="contact-line"><svg viewBox="0 0 20 20"><path d="M5 2l3 4-2 2c1 2 3 4 5 5l2-2 4 3-2 3C9 17 3 11 3 4z" fill="var(--navy)"/></svg><span>(242) 555-0148<br>(242) 555-0149</span></div>
    <div class="contact-line"><svg viewBox="0 0 20 20"><rect x="2" y="4" width="16" height="12" fill="none" stroke="var(--navy)" stroke-width="2"/><path d="M2 5l8 6 8-6" fill="none" stroke="var(--navy)" stroke-width="2"/></svg><span>info@tidewellcargo.example</span></div>
  </div>
  <div class="footer-col usa">
    <h4>USA</h4>
    <div class="contact-line"><svg viewBox="0 0 20 20"><path d="M10 1a6 6 0 0 1 6 6c0 5-6 12-6 12S4 12 4 7a6 6 0 0 1 6-6z" fill="var(--navy)"/><circle cx="10" cy="7" r="2" fill="#fff"/></svg><span>4120 NW 71st Street<br>Miami, Fl 33166</span></div>
    <div class="contact-line"><svg viewBox="0 0 20 20"><path d="M5 2l3 4-2 2c1 2 3 4 5 5l2-2 4 3-2 3C9 17 3 11 3 4z" fill="var(--navy)"/></svg><span>(305) 555-0172</span></div>
    <div class="contact-line"><svg viewBox="0 0 20 20"><rect x="2" y="4" width="16" height="12" fill="none" stroke="var(--navy)" stroke-width="2"/><path d="M2 5l8 6 8-6" fill="none" stroke="var(--navy)" stroke-width="2"/></svg><span>miami@tidewellcargo.example</span></div>
  </div>
  <div class="copyright">COPYRIGHT © 2018 TIDEWELL CARGO LINKS. ALL RIGHTS RESERVED.</div>
</footer>

</div>
</body>
</html>
```